Business cards for Marrowfield Consulting with the following info for the front side:

Marrowfield Consulting
Executive Coaching and Human Capital Strategy
www.marrowfield.example

Idalia Renvoort
Principal
idalia@marrowfield.example
+1 555 274 9186

Black background, text using the colours of the logo - enclosed.

The back side of the business card should feature the logo in the middle, with "Executive Coaching and Human Capital Strategy" on top and "www.marrowfield.example" below.

```html
<!DOCTYPE html>
<html lang="en">
<head>
<meta charset="utf-8">
<title>Marrowfield Consulting – Business Cards</title>
<link rel="stylesheet" href="https://fonts.googleapis.com/css2?family=Arimo:wght@400;700&display=swap">
<style>
  :root {
    --backdrop: #2b2b2d;
    --card: #0c0c0d;
    --card-edge: #161617;
    --blue: #29a8e0;
    --yellow: #fdbf1c;
    --grey: #b9b9bb;
    --white: #f2f2f2;
    --rule: #5a5a5c;
    --ring: rgba(255,255,255,0.045);
  }
  * { margin: 0; padding: 0; box-sizing: border-box; }
  html, body {
    width: 1200px; height: 900px; overflow: hidden;
    background: var(--backdrop);
    font-family: "Arimo", Arial, sans-serif;
  }
  .canvas {
    position: relative; width: 1200px; height: 900px;
    display: flex; flex-direction: column; align-items: center; justify-content: center;
    gap: 48px;
  }
  .card {
    position: relative; width: 640px; height: 366px;
    background: linear-gradient(160deg, var(--card-edge), var(--card) 60%);
    overflow: hidden;
    box-shadow: 0 10px 24px rgba(0,0,0,0.45);
  }
  .card__stripe {
    position: absolute; left: 0; right: 0; bottom: 0; height: 9px;
    display: flex;
  }
  .card__stripe span:first-child { flex: 1; background: var(--blue); }
  .card__stripe span:last-child { flex: 1; background: var(--yellow); }
  .card__ring {
    position: absolute; width: 300px; height: 300px; border-radius: 50%;
    border: 14px solid var(--ring);
    left: 50%; top: 50%; transform: translate(-50%, -50%);
  }

  /* Brand side */
  .brand__tagline {
    position: absolute; left: 248px; top: 58px;
    color: var(--grey); font-size: 17px; line-height: 1.15;
    text-transform: uppercase; letter-spacing: 0.3px;
  }
  .brand__mark {
    position: absolute; left: 0; right: 0; top: 150px;
    display: flex; align-items: center; justify-content: center; gap: 14px;
  }
  .brand__dot {
    width: 52px; height: 52px; border-radius: 50%;
    border: 3px solid var(--blue);
  }
  .brand__name {
    color: var(--blue); font-size: 46px; font-weight: 700; letter-spacing: 1px;
  }
  .brand__url {
    position: absolute; left: 0; right: 0; top: 272px; text-align: center;
    font-size: 19px; color: var(--blue);
  }
  .brand__url em { font-style: normal; color: var(--yellow); }

  /* Contact side */
  .contact { text-align: center; }
  .contact__name {
    position: absolute; left: 0; right: 0; top: 64px;
    color: var(--blue); font-size: 25px; font-weight: 700; letter-spacing: 0.5px;
    text-transform: uppercase;
  }
  .contact__role {
    position: absolute; left: 0; right: 0; top: 100px;
    color: var(--grey); font-size: 16px; letter-spacing: 0.5px; text-transform: uppercase;
  }
  .contact__divider {
    position: absolute; left: 170px; right: 170px; top: 136px;
    display: flex; align-items: center; gap: 8px;
  }
  .contact__divider::before, .contact__divider::after {
    content: ""; flex: 1; height: 1px; background: var(--rule);
  }
  .icon {
    width: 24px; height: 24px; border-radius: 4px;
    display: flex; align-items: center; justify-content: center;
  }
  .icon--blue { background: var(--blue); }
  .icon--yellow { background: var(--yellow); }
  .contact__lines {
    position: absolute; left: 0; right: 0; top: 166px;
    color: var(--white); font-size: 22px; line-height: 1.3; text-transform: uppercase;
  }
</style>
</head>
<body>
<main class="canvas">

  <section class="card brand" aria-label="Business card, brand side">
    <div class="card__ring" aria-hidden="true"></div>
    <p class="brand__tagline">Executive Coaching and<br>Human Capital Strategy</p>
    <div class="brand__mark">
      <span class="brand__dot" aria-hidden="true"></span>
      <span class="brand__name">MARROWFIELD</span>
    </div>
    <p class="brand__url">www.<em>marrowfield</em>.example</p>
    <div class="card__stripe"><span></span><span></span></div>
  </section>

  <section class="card contact" aria-label="Business card, contact side">
    <div class="card__ring" aria-hidden="true"></div>
    <h1 class="contact__name">Idalia Renvoort</h1>
    <p class="contact__role">Principal</p>
    <div class="contact__divider">
      <span class="icon icon--blue" aria-label="Phone">
        <svg width="16" height="16" viewBox="0 0 16 16"><path d="M3 2h3l1 3-2 1a8 8 0 0 0 5 5l1-2 3 1v3a1 1 0 0 1-1 1A12 12 0 0 1 2 3a1 1 0 0 1 1-1z" fill="#0c0c0d"/></svg>
      </span>
      <span class="icon icon--yellow" aria-label="Email">
        <svg width="16" height="16" viewBox="0 0 16 16"><rect x="2" y="4" width="12" height="8" fill="none" stroke="#0c0c0d" stroke-width="1.6"/><path d="M2 4l6 5 6-5" fill="none" stroke="#0c0c0d" stroke-width="1.6"/></svg>
      </span>
      <span class="icon icon--blue" aria-label="Website">
        <svg width="16" height="16" viewBox="0 0 16 16"><circle cx="8" cy="8" r="6" fill="none" stroke="#0c0c0d" stroke-width="1.5"/><ellipse cx="8" cy="8" rx="2.6" ry="6" fill="none" stroke="#0c0c0d" stroke-width="1.2"/><path d="M2 8h12" stroke="#0c0c0d" stroke-width="1.2"/></svg>
      </span>
    </div>
    <p class="contact__lines">
      +1 555 274 9186<br>
      idalia@marrowfield.example<br>
      www.marrowfield.example
    </p>
    <div class="card__stripe"><span></span><span></span></div>
  </section>

</main>
</body>
</html>
```